Design some Business Cards

Need some business cards made for new venture - website is varimest.com. I want to incorporate (in some fashion):

- logo (provided with name, and alone)
- website <p> font (Arvo )

Brian T. Holloway
BH VARIMEST
819 N. Garrick Ave. 3rd Floor
Chicago, IL 60647
brianh@varimest.com
(312) 448-2096
varimest.com

I am not very creative, hence the contest. Feel free to add design elements, but keep things consistent with the website (naturally). I am indifferent to one side vs. two-sided business card. I will be using PressNova, so you will want to use their Illustrator (or photoshop) templates located here:

http://www.pressnova-example.com/pn/ns/prodir/FileResources.aspx?pf_id=C41&selectedTab=0

The work product will be an Illustrator or Photoshop file, using the templates, with the winning design.

```html
<!DOCTYPE html>
<html lang="en">
<head>
<meta charset="utf-8">
<title>Varimest Business Cards</title>
<link rel="stylesheet" href="https://fonts.googleapis.com/css2?family=PT+Serif:wght@400;700&display=swap">
<style>
  :root {
    --backdrop: #2b2b2b;
    --card-dark: #0c0c0c;
    --card-light: #ffffff;
    --ink: #141414;
    --ink-soft: #2a2a2a;
    --on-dark: #f4f4f4;
    --rule: #1a1a1a;
  }
  * { margin: 0; padding: 0; box-sizing: border-box; }
  html, body {
    width: 1200px;
    height: 900px;
    overflow: hidden;
    background: var(--backdrop);
    font-family: "PT Serif", Georgia, serif;
  }
  .stage {
    width: 1200px;
    height: 900px;
    display: flex;
    align-items: center;
    justify-content: center;
    gap: 40px;
  }
  .card {
    width: 540px;
    height: 309px;
    position: relative;
    box-shadow: 0 10px 28px rgba(0,0,0,0.45);
  }

  /* Front side */
  .card-front {
    background: var(--card-dark);
    display: flex;
    align-items: center;
    justify-content: center;
  }
  .front-brand {
    display: flex;
    align-items: center;
    gap: 14px;
    color: var(--on-dark);
    font-weight: 700;
    font-size: 40px;
    letter-spacing: 0.5px;
  }
  .front-brand .dot {
    width: 26px;
    height: 26px;
    border-radius: 50%;
    background: var(--on-dark);
  }

  /* Back side */
  .card-back {
    background: var(--card-light);
    color: var(--ink);
  }
  .back-brand {
    position: absolute;
    top: 36px;
    right: 40px;
    display: flex;
    align-items: center;
    gap: 10px;
  }
  .back-brand .dot {
    width: 24px;
    height: 24px;
    border-radius: 50%;
    background: var(--ink);
  }
  .back-brand .divider {
    width: 1px;
    height: 30px;
    background: var(--rule);
  }
  .back-brand .name {
    font-weight: 700;
    font-size: 30px;
    color: var(--ink);
    line-height: 1;
  }

  .holder {
    position: absolute;
    top: 112px;
    left: 0;
    display: flex;
    align-items: stretch;
    gap: 12px;
  }
  .holder .marker {
    width: 20px;
    margin-left: 30px;
    background: var(--ink);
  }
  .holder .person {
    font-weight: 700;
    font-size: 17px;
    line-height: 1.2;
  }
  .holder .role {
    font-size: 11px;
    letter-spacing: 0.4px;
    margin-top: 2px;
    color: var(--ink-soft);
  }

  .contact {
    position: absolute;
    left: 62px;
    bottom: 30px;
    font-size: 12px;
    line-height: 1.55;
    color: var(--ink-soft);
  }
  .contact .address { margin-bottom: 4px; }
  .contact .line {
    display: flex;
    align-items: center;
    gap: 8px;
  }
  .contact svg {
    width: 11px;
    height: 11px;
    fill: var(--ink);
    flex: none;
  }
</style>
</head>
<body>
<main class="stage">
  <section class="card card-front" aria-label="Card front">
    <div class="front-brand">
      <span class="dot"></span>
      <span>varimest</span>
    </div>
  </section>

  <section class="card card-back" aria-label="Card back">
    <div class="back-brand">
      <span class="dot"></span>
      <span class="divider"></span>
      <span class="name">varimest</span>
    </div>

    <div class="holder">
      <span class="marker"></span>
      <div>
        <p class="person">Brian T. Holloway</p>
        <p class="role">BH VARIMEST</p>
      </div>
    </div>

    <div class="contact">
      <div class="address">
        <p>819 N. Garrick Ave. 3rd Floor</p>
        <p>Chicago, IL 60647</p>
      </div>
      <p class="line">
        <svg viewBox="0 0 24 24" aria-hidden="true"><path d="M6.6 10.8a15.1 15.1 0 0 0 6.6 6.6l2.2-2.2a1 1 0 0 1 1-.25 11.4 11.4 0 0 0 3.6.57 1 1 0 0 1 1 1V20a1 1 0 0 1-1 1A17 17 0 0 1 3 4a1 1 0 0 1 1-1h3.5a1 1 0 0 1 1 1c0 1.25.2 2.45.57 3.57a1 1 0 0 1-.25 1z"/></svg>
        (312) 448-2096
      </p>
      <p class="line">
        <svg viewBox="0 0 24 24" aria-hidden="true"><path d="M2 11 22 2l-9 20-2.5-8.5z"/></svg>
        brianh@varimest.com
      </p>
      <p class="line">
        <svg viewBox="0 0 24 24" aria-hidden="true"><path d="M12 2a10 10 0 1 0 0 20 10 10 0 0 0 0-20zm6.9 6h-2.9a15.6 15.6 0 0 0-1.4-3.6A8 8 0 0 1 18.9 8zM12 4a14 14 0 0 1 1.9 4h-3.8A14 14 0 0 1 12 4zM4.3 14a8 8 0 0 1 0-4h3.4a16 16 0 0 0 0 4zm.8 2h2.9a15.6 15.6 0 0 0 1.4 3.6A8 8 0 0 1 5.1 16zM8 8H5.1a8 8 0 0 1 4.3-3.6A15.6 15.6 0 0 0 8 8zm4 12a14 14 0 0 1-1.9-4h3.8A14 14 0 0 1 12 20zm2.3-6H9.7a14.6 14.6 0 0 1 0-4h4.6a14.6 14.6 0 0 1 0 4zm.3 5.6A15.6 15.6 0 0 0 16 16h2.9a8 8 0 0 1-4.3 3.6zM16.3 14a16 16 0 0 0 0-4h3.4a8 8 0 0 1 0 4z"/></svg>
        varimest.com
      </p>
    </div>
  </section>
</main>
</body>
</html>
```